Velmora Power

We need a business card for "Velmora power". I have uploaded the logo, the color of the card should be according to the logo "Blackish".
Basically velmora power is a solar company.
Also we would like a sample file in which we can edit the information such names and contact details ourselves
The card would be two sided with following details
1- logo on front and underneath the logo there should be a line saying
"Cleaner . Cheaper . Power"
2-website i.e "www.velmorapower.example"
3- Icons for Facebook and Instagram that tells the clients we are available on both social sites.
4- name of the person with his/her designation underneath and email address
5-contact number
6- 1-800--- number with the extension number

its up to the designer how he/she places the details,but it must look professional

5-contact number

Requirements
Must have
• 1- logo on front and underneath the logo there should be a line saying
• "Cleaner . Cheaper . Power"
• 2-website i.e "www.velmorapower.example"
• 3- Icons for Facebook and Instagram that tells the clients we are available on both social sites.
• 4- name of the person with his/her designation underneath and email address
• 5-contact number of the person
• 6- 1-800--- number with the extension number
• 7-card should be in black shade like the logo

```html
<!DOCTYPE html>
<html lang="en">
<head>
<meta charset="utf-8">
<title>Velmora Power — Business Card</title>
<link rel="stylesheet" href="https://fonts.googleapis.com/css2?family=Open+Sans:wght@400;600&family=Montserrat:wght@700&display=swap">
<style>
  :root {
    --canvas: #e9e7e2;
    --card-black: #141414;
    --card-black-edge: #262626;
    --card-white: #ffffff;
    --brand-green: #7dc243;
    --band-grey: #4a4a4a;
    --text-grey: #555555;
    --text-light: #f2f2f2;
  }
  * { margin: 0; padding: 0; box-sizing: border-box; }
  html, body {
    width: 771px; height: 1200px; overflow: hidden;
    background: var(--canvas);
    font-family: "Open Sans", Arial, sans-serif;
  }
  .sheet {
    width: 771px; height: 1200px;
    display: flex; flex-direction: column; align-items: center; justify-content: center;
    gap: 80px;
  }
  .card {
    position: relative; width: 640px; height: 366px; overflow: hidden;
    box-shadow: 0 10px 28px rgba(0,0,0,.22);
  }

  /* ---------- Back: details side ---------- */
  .card--details { background: var(--card-white); }
  .brand-mark {
    display: flex; align-items: center; gap: 10px;
    font-family: "Montserrat", Arial, sans-serif; font-weight: 700;
    color: var(--brand-green); letter-spacing: .5px; white-space: nowrap;
  }
  .brand-mark__square { width: 18px; height: 18px; background: var(--brand-green); flex: none; }
  .card--details .brand-mark { position: absolute; top: 62px; right: 56px; font-size: 28px; }

  .person { position: absolute; left: 40px; top: 158px; padding-left: 14px; border-left: 5px solid var(--brand-green); }
  .person__name { font-size: 24px; color: var(--text-grey); line-height: 1.1; }
  .person__title { font-size: 13px; color: var(--brand-green); margin-top: 4px; }

  .contact-list { position: absolute; left: 210px; top: 160px; list-style: none; }
  .contact-list li { display: flex; align-items: center; gap: 12px; font-size: 13px; color: var(--text-grey); margin-bottom: 10px; white-space: nowrap; }
  .contact-list svg { width: 15px; height: 15px; flex: none; }
  .contact-rule { position: absolute; left: 210px; top: 262px; width: 230px; height: 2px; background: var(--brand-green); }

  .footer-band { position: absolute; left: 0; right: 0; bottom: 0; height: 44px; display: flex; }
  .footer-band__social {
    flex: 1; background: var(--band-grey); display: flex; align-items: center; gap: 26px; padding-left: 100px;
    color: var(--text-light); font-size: 13px; white-space: nowrap;
  }
  .social { display: flex; align-items: center; gap: 8px; }
  .social__square { width: 13px; height: 13px; background: var(--brand-green); flex: none; }
  .footer-band__web {
    width: 240px; flex: none; background: var(--brand-green); color: #fff; font-size: 13px;
    display: flex; align-items: center; justify-content: center; margin-left: 10px; white-space: nowrap;
  }

  /* ---------- Front: logo side ---------- */
  .card--logo { background: linear-gradient(160deg, var(--card-black-edge), var(--card-black) 55%); }
  .card--logo .brand-mark { position: absolute; left: 120px; top: 128px; font-size: 44px; gap: 14px; }
  .card--logo .brand-mark__square { width: 26px; height: 26px; }
  .tagline { position: absolute; left: 300px; top: 206px; font-size: 17px; color: var(--text-light); letter-spacing: .3px; white-space: nowrap; }
  .tagline-rule { position: absolute; left: 300px; top: 238px; width: 212px; height: 2px; background: var(--brand-green); }
</style>
</head>
<body>
<main class="sheet">

  <section class="card card--details" aria-label="Card back with contact details">
    <div class="brand-mark"><span class="brand-mark__square"></span>Velmora Power</div>

    <div class="person">
      <p class="person__name">Your Name</p>
      <p class="person__title">Job Title</p>
    </div>

    <ul class="contact-list">
      <li>
        <svg viewBox="0 0 16 16"><path fill="#7dc243" d="M3 1h3l1.5 4-2 1.3a9 9 0 0 0 4.2 4.2L11 8.5l4 1.5v3a2 2 0 0 1-2 2A12 12 0 0 1 1 3a2 2 0 0 1 2-2z"/></svg>
        1-800-000-0000 Ext. 000
      </li>
      <li>
        <svg viewBox="0 0 16 16"><rect x="4" y="1" width="8" height="14" rx="1.5" fill="none" stroke="#888" stroke-width="1.4"/><circle cx="8" cy="12.5" r=".9" fill="#888"/></svg>
        000 000 0000
      </li>
      <li>
        <svg viewBox="0 0 16 16"><rect x="1" y="3" width="14" height="10" fill="#7dc243"/><path d="M1 3l7 6 7-6" fill="none" stroke="#fff" stroke-width="1.3"/></svg>
        youremail@velmorapower.example
      </li>
    </ul>
    <div class="contact-rule"></div>

    <div class="footer-band">
      <div class="footer-band__social">
        <span class="social"><span class="social__square"></span>/velmora.social</span>
        <span class="social"><span class="social__square"></span>/velmora.photos</span>
      </div>
      <div class="footer-band__web">www.velmorapower.example</div>
    </div>
  </section>

  <section class="card card--logo" aria-label="Card front with logo and tagline">
    <div class="brand-mark"><span class="brand-mark__square"></span>Velmora Power</div>
    <p class="tagline">Cleaner . Cheaper . Power</p>
    <div class="tagline-rule"></div>
  </section>

</main>
</body>
</html>
```